Modern CNC Machining Facility in Need of Web Site Improvement

Brixton Fabrication and Tooling, LLC is in need of a web site update. We need to highlight both product sales and our manufacturing services offered. We have recently started offering online product sales and need a better ecommerce platform for our customers. We would like the design winner to be able to freelance the project to a fully functioning webpage.
www.brixtonfabrication.example
What we like about our current web site:
Black and red highlight colors
Gear and caliper logo
RNVR Veteran owned business
What we don't like about our current web site:
Unorganized
Doesn't stand out
Looks like it was made in 1995
Online Product sales are awkward

```html
<!DOCTYPE html>
<html lang="en">
<head>
<meta charset="utf-8">
<title>Brixton Fabrication and Tooling, LLC</title>
<link href="https://fonts.googleapis.com/css2?family=Arimo:wght@400;700&display=swap" rel="stylesheet">
<style>
:root{
  --red:#b5161d;
  --red-dark:#8e0f14;
  --ink:#231f20;
  --nav:#1f1d1e;
  --grey:#5a5a5a;
  --grey-mid:#7a7a7a;
  --text:#555;
  --muted:#888;
  --page:#f2f0f0;
  --white:#fff;
  --line:#e2e0e0;
  --gold:#f5c518;
}
*{box-sizing:border-box;margin:0;padding:0}
html,body{width:1200px;height:1108px;overflow:hidden}
body{font-family:"Arimo",Arial,sans-serif;color:var(--text);background:var(--page)}
.canvas{position:relative;width:1200px;height:1108px;overflow:hidden}
.sc{font-variant:small-caps}
.abs{position:absolute}

/* header */
.site-header{position:absolute;left:0;top:0;width:1200px;height:126px;background:var(--white);border-bottom:1px solid var(--line)}
.brand{position:absolute;left:314px;top:19px;display:flex;align-items:center;gap:10px}
.brand-mark{width:46px;height:46px;border-radius:50%;background:var(--ink)}
.brand-name{font-size:14px;font-weight:700;color:var(--red);font-variant:small-caps;letter-spacing:.2px}
.brand-tag{font-size:8.5px;color:#333;margin-top:3px}
.service{position:absolute;right:310px;top:4px;font-size:9px;color:#999}
.service b{color:var(--red);font-size:10px}
.account{position:absolute;right:310px;top:27px;font-size:7.5px;color:#555;text-align:right;line-height:14px}
.account a{color:var(--red);text-decoration:none;font-weight:700}
.account .cart{color:#999}
.main-nav{position:absolute;left:314px;top:80px;width:576px;height:37px;background:var(--nav);display:flex}
.main-nav a{flex:1 1 auto;display:flex;align-items:center;justify-content:center;font-size:9px;font-weight:700;color:var(--white);text-decoration:none;font-variant:small-caps;border-right:1px solid #3a3839}
.main-nav a.active{background:linear-gradient(#c91e25,var(--red-dark));flex:0 0 65px}

/* sidebar */
.panel{position:absolute;left:314px;width:113px;background:var(--white)}
.search{top:133px;height:28px;display:flex;align-items:center;padding:0 10px;font-size:7px;color:#aaa;justify-content:space-between}
.categories{top:166px;height:205px;padding:7px 7px}
.red-title{background:linear-gradient(#cc2128,var(--red-dark));color:var(--white);font-size:8px;font-weight:700;font-variant:small-caps;padding:7px 6px;height:25px}
.categories ul{list-style:none;padding:0 5px}
.categories li{font-size:6.5px;font-weight:700;color:#666;padding:6px 0;border-bottom:1px solid #eee}
.my-cart{top:378px;height:64px;background:var(--red-dark)}
.my-cart h3,.compare h3{font-size:8.5px;font-weight:700;color:var(--white);font-variant:small-caps;padding:8px 11px;background:var(--red);height:24px}
.my-cart p,.compare p{font-size:6.5px;color:var(--white);padding:8px 11px;line-height:10px}
.links{top:449px;height:160px;padding:14px 9px}
.links h3{font-size:8.5px;font-weight:400;color:#333;font-variant:small-caps;margin-bottom:12px}
.links ul{list-style:none}
.links li{font-size:6.5px;font-weight:700;color:var(--red);display:flex;align-items:center;gap:7px;margin-bottom:7px}
.links li::before{content:"";width:8px;height:8px;border-radius:50%;background:#bbb}
.btn-dark{display:inline-block;background:var(--grey);color:var(--white);font-size:6px;font-weight:700;padding:7px 13px}
.compare{top:624px;height:64px;background:var(--grey-mid)}
.compare h3{background:linear-gradient(#6a6a6a,#4a4a4a)}
.tweets{top:695px;height:217px;padding:14px 9px}
.tweets h3{display:flex;align-items:center;gap:9px;font-size:8.5px;font-weight:400;color:#333;font-variant:small-caps;padding-bottom:12px;border-bottom:1px solid #eee}
.tweets h3 i{width:14px;height:14px;border-radius:50%;background:#888;display:block}
.tweet{padding:12px 0 10px;border-bottom:1px solid #eee;font-size:6px;line-height:9px}
.tweet a{color:#2a8ec9;text-decoration:none;display:block}
.tweet em{display:block;color:#aaa;margin-top:10px}

/* banner */
.banner{position:absolute;left:433px;top:133px;width:457px;height:202px;background:radial-gradient(circle at 30% 40%,#6d5d64,#3a2a30 60%,#5a2b3b)}
.promo{position:absolute;left:233px;top:73px;width:202px;height:86px;background:rgba(255,255,255,.18);text-align:center;padding-top:9px}
.promo h2{font-size:23px;font-weight:400;color:var(--white)}
.promo p{font-size:11px;font-weight:700;color:var(--gold)}
.promo span{display:inline-block;margin-top:9px;background:var(--white);color:#222;font-size:6.5px;font-weight:700;padding:6px 10px}
.tabs{position:absolute;left:433px;top:335px;width:457px;height:29px;display:flex;background:var(--ink)}
.tabs span{flex:1;display:flex;align-items:center;justify-content:center;font-size:6.5px;font-weight:700;color:#777;border-right:1px solid #444}
.tabs span.on{background:var(--red);color:var(--white);position:relative}
.tabs span.on::before{content:"";position:absolute;top:-6px;left:50%;margin-left:-6px;border:6px solid transparent;border-top:0;border-bottom-color:var(--red)}

/* center */
.intro{position:absolute;left:433px;top:369px;width:340px;height:145px;background:linear-gradient(var(--white),#f4f3f3);padding:18px 10px}
.intro h1{font-size:10px;font-weight:400;color:#222;font-variant:small-caps;margin-bottom:12px}
.intro p{font-size:5.8px;line-height:11px;color:#666;margin-bottom:8px}
.products{position:absolute;left:433px;top:515px;width:340px;height:402px;background:var(--white);padding:15px 10px}
.products h2{font-size:8.5px;font-weight:400;color:#333;font-variant:small-caps;margin-bottom:12px}
.card{display:flex;height:118px;background:linear-gradient(#f6f4f4,var(--white));margin-bottom:3px;padding:17px 16px}
.thumb{width:91px;height:67px;margin-right:18px;flex:none}
.card h4{font-size:6.8px;font-weight:400;color:var(--red);margin-bottom:6px}
.card p{font-size:5.7px;line-height:11.5px;color:#888}
.price{font-size:7.5px;color:#333;margin:6px 0 9px}
.btns{display:flex;gap:3px}
.btn-red,.btn-grey{font-size:5.8px;font-weight:700;color:var(--white);width:50px;height:16px;display:flex;align-items:center;justify-content:center}
.btn-red{background:var(--red)}
.btn-grey{background:linear-gradient(#777,#555)}

/* special */
.special{position:absolute;left:777px;top:369px;width:113px;height:553px;background:var(--white)}
.special h3{height:23px;background:linear-gradient(#8a8a8a,#4e4e4e);color:var(--white);font-size:8px;font-weight:700;font-variant:small-caps;padding:7px 8px}
.sp-item{height:133px;padding:10px 8px 0;border-bottom:3px solid var(--page)}
.sp-img{width:58px;height:52px;margin:0 auto 8px;border-radius:50%;background:radial-gradient(circle,#9aa08a,#6b4a33)}
.sp-item h4{font-size:6.5px;font-weight:400;color:var(--red)}
.sp-price{display:flex;justify-content:space-between;font-size:7.5px;color:#333;margin:5px 0 8px}
.sp-price s{color:#777}
.sp-item .btn-red,.sp-item .btn-grey{width:47px}

/* features */
.features{position:absolute;left:314px;top:938px;width:576px;height:46px;background:var(--white);border:1px solid #ddd;display:flex;align-items:center}
.feature{flex:1;display:flex;align-items:center;justify-content:center;gap:10px;border-right:1px solid #e4e4e4;height:26px}
.feature:last-child{border:0}
.feature b{display:block;font-size:9px;font-weight:400;color:var(--red)}
.feature span{font-size:9px;color:#555}

/* footer */
.site-footer{position:absolute;left:0;top:994px;width:1200px;height:114px;background:var(--ink);color:#ccc}
.foot-brand{position:absolute;left:314px;top:22px;display:flex;align-items:center;gap:8px;font-size:9px;font-weight:700;color:var(--white)}
.foot-brand i{width:44px;height:44px;border-radius:50%;background:var(--white);display:block}
.copy{position:absolute;left:314px;top:78px;font-size:6.5px;color:var(--white);font-weight:700}
.copy span{font-weight:400;color:#999}
.foot-col{position:absolute;top:22px}
.foot-col h4{font-size:10px;font-weight:400;color:var(--white);font-variant:small-caps;margin-bottom:12px}
.foot-col li{list-style:none;font-size:6.5px;color:#aaa;margin-bottom:8px}
.foot-col li::before{content:"› ";color:#888}
.addr{font-size:6.5px;color:#aaa;line-height:12px;font-weight:700}
.call{font-size:9px;color:#ccc;font-weight:700;margin-top:9px}
</style>
</head>
<body>
<div class="canvas">

<header class="site-header">
  <div class="brand">
    <div class="brand-mark"></div>
    <div>
      <div class="brand-name">Brixton Fabrication and Tooling, LLC</div>
      <div class="brand-tag">CNC Milling &amp; Turning, Production Machining, Ice Fishing Spears</div>
    </div>
  </div>
  <div class="service">Customer Service: <b>1-800-555-0199</b></div>
  <div class="account"><span>My Account</span> | <a href="#">Login</a><br><span class="cart">&#128722; MY CART: 0 ITEM(S) - $0.00 &#709;</span></div>
  <nav class="main-nav">
    <a class="active" href="#">Home</a>
    <a href="#">Online Product Sales</a>
    <a href="#">Ice Fishing Spears</a>
    <a href="#">About Us</a>
    <a href="#">Equipment</a>
    <a href="#">Contact Us</a>
    <a href="#">Blog</a>
  </nav>
</header>

<aside>
  <div class="panel search">Search
    <svg width="10" height="10" viewBox="0 0 10 10"><circle cx="4" cy="4" r="3" fill="none" stroke="#bbb" stroke-width="1.2"/><line x1="6.2" y1="6.2" x2="9.5" y2="9.5" stroke="#bbb" stroke-width="1.4"/></svg>
  </div>
  <div class="panel categories">
    <div class="red-title">Lorem ipsum dolor</div>
    <ul>
      <li>Lorem ipsum dolor</li><li>Lorem sit amet</li><li>Lorem ipsum dolor</li><li>Lorem ipsum sit amet</li>
      <li>Lorem ipsum dolor</li><li>Lorem ipsum dolor sit amet</li><li>Lorem ipsum</li><li>Lorem ipsum sit</li>
    </ul>
  </div>
  <div class="panel my-cart"><h3>My Cart</h3><p>You have no item in your shopping cart</p></div>
  <div class="panel links">
    <h3>Lorem Ipsum</h3>
    <ul><li>Lorem ipsum</li><li>Lorem ipsum sit</li><li>Lorem dolor sit</li><li>Lorem ipsum</li><li>Lorem ipsum dolor sit</li></ul>
    <span class="btn-dark" style="margin-top:10px">VIEW ALL</span>
  </div>
  <div class="panel compare"><h3>Compare Products</h3><p>You have no item to compare</p></div>
  <div class="panel tweets">
    <h3><i></i>Latest Tweet</h3>
    <div class="tweet"><a href="#">http://example.com/abc/abc</a>Lorem ipsum dolor sit amet, consectetur adipiscing elit, sed do eiusmod tempor<em>2 min ago</em></div>
    <div class="tweet"><a href="#">http://example.com/abc/abc</a>Lorem ipsum dolor sit amet, consectetur adipiscing elit, sed do eiusmod tempor<em>2 min ago</em></div>
    <span class="btn-dark" style="margin-top:12px">VIEW ALL</span>
  </div>
</aside>

<section class="banner" role="img" aria-label="Close-up photo of machined steel gears">
  <div class="promo"><h2>Click &amp; Save</h2><p>Buy 1 item &amp; Get 50%</p><span>SHOP NOW !</span></div>
</section>
<div class="tabs"><span class="on">Lorem ipsum dolor</span><span>Lorem ipsum dolor</span><span>Lorem ipsum dolor</span><span>Lorem ipsum dolor</span></div>

<section class="intro">
  <h1>Lorem ipsum dolor</h1>
  <p><b>Your Manufacturing Experts.</b><br>We are your CNC milling and turning go-to facility. Our manufacturing facility is located in Port Alden, Michigan and is equipped to perform a variety of machining services, including three axis CNC milling, "lights out" CNC turning, CNC Plasma Cutting, fully automatic sawing, prototype machining, long and short run production.</p>
  <p>Brixton Fabrication is proudly owned and operated by Daniel and Peter Lasko. We have the capability, experience and know-how to solve even your most complex manufacturing problems. We stand behind the services we offer and guarantee your satisfaction.</p>
</section>

<section class="products">
  <h2>New Products</h2>
  <div class="card">
    <div class="thumb" role="img" aria-label="Photo of a gear clock with wings" style="background:linear-gradient(135deg,#8a7a5e,#4d4033)"></div>
    <div><h4>GEAR CLOCK WITH WINGS</h4><p>CNC plasma cut clock with a rust patina. Clear coat finish.<br>Material is 16ga steel. Approximate Dimensions Are 28" x 12".<br>Made in Michigan by Brixton Fabrication and Tooling, LLC</p>
    <div class="price">$155.00</div><div class="btns"><span class="btn-red">Add to Cart</span><span class="btn-grey">Detail</span></div></div>
  </div>
  <div class="card">
    <div class="thumb" role="img" aria-label="Photo of a triple gear clock" style="background:radial-gradient(circle,#8f9479,#6b4a33 70%,#f6f4f4 72%)"></div>
    <div><h4>TRIPLE GEAR CLOCK</h4><p>CNC plasma cut clock with a rust patina. Clear coat finish.<br>Material is 16ga steel. Approximate Dimensions Are 21" x 12".<br>Made in Michigan by Brixton Fabrication and Tooling, LLC</p>
    <div class="price">$155.00</div><div class="btns"><span class="btn-red">Add to Cart</span><span class="btn-grey">Detail</span></div></div>
  </div>
  <div class="card">
    <div class="thumb" role="img" aria-label="Photo of a black sun clock" style="background:radial-gradient(circle,#bbb,#2c2c2c 45%,#d8d8d8 75%)"></div>
    <div><h4>SUN CLOCK</h4><p>CNC plasma cut clock with a rust patina. Clear coat finish.<br>Material is 16ga steel. Approximate Dimensions Are 29" x 12".<br>Made in Michigan by Brixton Fabrication and Tooling, LLC</p>
    <div class="price">$155.00</div><div class="btns"><span class="btn-red">Add to Cart</span><span class="btn-grey">Detail</span></div></div>
  </div>
</section>

<section class="special">
  <h3>Special</h3>
  <div class="sp-item"><div class="sp-img" role="img" aria-label="Photo of a triple gear clock"></div><h4>TRIPLE GEAR CLOCK</h4><div class="sp-price">$155.00 <s>$255.00</s></div><div class="btns"><span class="btn-red">Add to Cart</span><span class="btn-grey">Detail</span></div></div>
  <div class="sp-item"><div class="sp-img" role="img" aria-label="Photo of a triple gear clock"></div><h4>TRIPLE GEAR CLOCK</h4><div class="sp-price">$155.00 <s>$255.00</s></div><div class="btns"><span class="btn-red">Add to Cart</span><span class="btn-grey">Detail</span></div></div>
  <div class="sp-item"><div class="sp-img" role="img" aria-label="Photo of a triple gear clock"></div><h4>TRIPLE GEAR CLOCK</h4><div class="sp-price">$155.00 <s>$255.00</s></div><div class="btns"><span class="btn-red">Add to Cart</span><span class="btn-grey">Detail</span></div></div>
  <div class="sp-item" style="border:0"><div class="sp-img" role="img" aria-label="Photo of a triple gear clock"></div><h4>TRIPLE GEAR CLOCK</h4><div class="sp-price">$155.00 <s>$255.00</s></div><div class="btns"><span class="btn-red">Add to Cart</span><span class="btn-grey">Detail</span></div></div>
</section>

<section class="features">
  <div class="feature">
    <svg width="20" height="20" viewBox="0 0 20 20"><rect x="2" y="9" width="4" height="9" fill="#aaa"/><path d="M7 9 L11 2 Q13 2 12.5 6 L12 8 H17 Q18.5 8.5 18 10 L16 17 Q15.5 18 14 18 H7 Z" fill="#aaa"/></svg>
    <div><b>SATISFACTION</b><span>100% Guaranteed</span></div>
  </div>
  <div class="feature">
    <svg width="20" height="20" viewBox="0 0 20 20"><path d="M3 10 L11 2 H18 V9 L10 17 Z" fill="#aaa"/><circle cx="14.5" cy="5.5" r="1.5" fill="#fff"/></svg>
    <div><b>LOWEST PRICE</b><span>Guaranteed</span></div>
  </div>
  <div class="feature">
    <svg width="18" height="20" viewBox="0 0 18 20"><path d="M5 9 V6 a4 4 0 0 1 8 0 V9" fill="none" stroke="#aaa" stroke-width="2"/><rect x="2" y="9" width="14" height="10" fill="#aaa"/></svg>
    <div><b>SECURE</b><span>Shopping</span></div>
  </div>
  <div class="feature">
    <svg width="22" height="18" viewBox="0 0 22 18"><path d="M4 8 a5 4 0 0 1 5-4 H17 M14 1 L17 4 L14 7" fill="none" stroke="#aaa" stroke-width="2"/><path d="M18 10 a5 4 0 0 1 -5 4 H5 M8 11 L5 14 L8 17" fill="none" stroke="#aaa" stroke-width="2"/></svg>
    <div><b>30 - DAYS</b><span>Easy Return</span></div>
  </div>
</section>

<footer class="site-footer">
  <div class="foot-brand"><i></i>Brixton Fabrication</div>
  <div class="copy">COMPANY NAME &nbsp;© 2014 <span>| PRIVACY POLICY</span></div>
  <div class="foot-col" style="left:516px"><h4>Lorem Ipsum</h4><ul><li>Lorem ipsum dolor</li><li>Lorem ipsum dolor sit amet</li><li>Lorem ipsum sit amet</li><li>Lorem sit amet</li></ul></div>
  <div class="foot-col" style="left:640px"><h4>Lorem Ipsum</h4><ul><li>Lorem sit amet</li><li>Lorem sit amet</li><li>Lorem sit amet</li></ul></div>
  <div class="foot-col" style="left:769px"><h4>Location</h4><div class="addr">1420 Harbor Mill Rd<br>Port Alden MI, 48790</div><div class="call">CALL: 1234 5550 9000</div></div>
</footer>

</div>
</body>
</html>
```